Produktflyer für zwei ERP-Schnittstellen (Kalvero)

Wir haben zwei Schnittstellen entwickelt, die wir gerne Promoten möchten. Infos zu den zwei Produkten sind in den angehängten PowerPoints. Wir hätten gerne Design Vorschläge für ein Factsheet.
Unser logo ist angehängt. Wir sind aktuell daran eine neue Homepage zu erarbeiten. Das Mockup kann hier gefunden werden:
https://www.entwurfsraum.example/proto/Q7HK294jw3xbnmoL58Tz2k/BrendoSoftware?page-id=0%3A1&node-id=1-59&p=f&viewport=-598%2C57%2C0.12&t=XyPk4mNbQ8zAeLFd-1&scaling=scale-down-width&content-scaling=fixed&starting-point-node-id=1%3A551
Kalvero Benutzer die an Ferna, Useko oder Talvun liefern. Bzw. Waffenhändler
- Roboto

```html
<!DOCTYPE html>
<html lang="de">
<head>
<meta charset="utf-8">
<title>Factsheets – Brendo Software</title>
<link href="https://fonts.googleapis.com/css2?family=Roboto:wght@400;500;700;900&display=swap" rel="stylesheet">
<style>
:root{
  --stage:#a9a9a9;
  --blue:#1565c0;
  --blue-dark:#0d4f9e;
  --blue-light:#eaf2fb;
  --tri:#cfe0f5;
  --ink:#1d1d1f;
  --text:#2b2b2b;
  --black:#0c0c0c;
  --white:#ffffff;
}
*{box-sizing:border-box;margin:0;padding:0}
html,body{width:828px;height:1200px;overflow:hidden;background:var(--stage)}
body{font-family:'Roboto',sans-serif;color:var(--text);position:relative}
.sheet-slot{position:absolute;top:323px;width:392px;height:553px;overflow:hidden;box-shadow:0 2px 6px rgba(0,0,0,.15)}
.slot-left{left:15px}
.slot-right{left:421px}
.flyer{position:absolute;left:0;top:0;width:704px;height:993px;transform:scale(.5568);transform-origin:0 0;overflow:hidden;background:linear-gradient(180deg,#f1f3f7 0,#fff 260px)}
.decor{position:absolute;left:0;top:0}
.brand{position:absolute;display:flex;align-items:center;gap:9px}
.brand-dot{width:34px;height:34px;border-radius:50%;background:var(--blue)}
.brand-name{font-size:29px;font-weight:700;color:var(--ink);line-height:1}
.brand-tag{font-size:10.5px;font-weight:500;color:var(--blue);letter-spacing:.6px;margin-top:3px}
.rule{position:absolute;height:3px;background:var(--blue)}
.title{position:absolute;font-weight:700;color:var(--ink)}
.title .product{color:var(--blue)}
.photo{position:absolute}
.band{position:absolute;left:0;width:704px;background:var(--blue)}
.intro{position:absolute;color:var(--white);font-size:13.5px;line-height:17px}
.panel{position:absolute;background:var(--blue-light)}
.section-head{position:absolute;font-size:17px;font-weight:500;color:var(--blue);white-space:nowrap}
.section-head svg{position:absolute;left:0;top:-4px}
.bullets{position:absolute;list-style:none;font-size:14px;color:var(--text)}
.bullets li{position:relative;padding-left:18px}
.bullets li::before{content:"";position:absolute;left:0;top:6px;width:10px;height:10px;border-radius:50%;background:var(--blue)}
.bullets li::after{content:"";position:absolute;left:2.6px;top:8.4px;width:4.6px;height:2.6px;border-left:1.5px solid #fff;border-bottom:1.5px solid #fff;transform:rotate(-45deg)}
.body-text{position:absolute;font-size:14px;line-height:17px;color:var(--text)}
.footer-black{position:absolute;left:0;top:858px;width:704px;height:135px;background:var(--black)}
.footer-blue{position:absolute;left:364px;top:815px;width:340px;height:178px;background:linear-gradient(135deg,var(--blue) 0,var(--blue-dark) 100%)}
.company{position:absolute;left:392px;top:846px;color:var(--white)}
.company h2{font-size:24px;font-weight:500;margin-bottom:6px;white-space:nowrap}
.contact{list-style:none;font-size:14px;line-height:22.5px}
.contact li{display:flex;align-items:center;gap:8px;white-space:nowrap}
</style>
</head>
<body>

<!-- EDI factsheet -->
<div class="sheet-slot slot-left">
<main class="flyer">
  <svg class="decor" width="704" height="993" aria-hidden="true">
    <polygon points="388,265 414,222 440,265" fill="var(--tri)"/>
    <polygon points="674,265 700,222 704,228 704,265" fill="var(--tri)"/>
    <polygon points="314,640 340,596 366,640" fill="var(--tri)" opacity=".6"/>
    <polygon points="0,872 704,800 704,820 0,892" fill="var(--blue)"/>
  </svg>

  <div class="brand" style="left:54px;top:46px">
    <span class="brand-dot"></span>
    <div><div class="brand-name">BrendoSoftware</div><div class="brand-tag">BUSINESS &amp; SOFTWARE</div></div>
  </div>
  <div class="rule" style="left:61px;top:114px;width:150px"></div>

  <h1 class="title" style="left:55px;top:143px;font-size:28px;line-height:34px"><span class="product">LinkEDI -</span> Automatisierter<br>EDI-Datenaustausch mit<br>Grossverteilern</h1>

  <svg class="photo" style="left:380px;top:8px" width="322" height="258" role="img" aria-label="Foto: zwei Personen verpacken Bestellungen an einem Laptop in einem Lager mit Kartons">
    <defs><linearGradient id="edi-top" x1="0" y1="0" x2="1" y2="1"><stop offset="0" stop-color="#e7e2da"/><stop offset=".5" stop-color="#b99a74"/><stop offset="1" stop-color="#6d5a4a"/></linearGradient></defs>
    <polygon points="80,0 240,0 319,129 240,258 80,258 2,129" fill="url(#edi-top)"/>
  </svg>

  <div class="band" style="top:265px;height:102px"></div>
  <p class="intro" style="left:40px;top:283px;width:624px;text-align:center">Mit LinkEDI bietet die Brendo Software GmbH eine leistungsstarke Lösung für Unternehmen, die ihre Auftragsabwicklung mit Grossverteilern wie Talvun, Varno oder Ferna digitalisieren möchten. Die Schnittstelle empfängt Bestellungen und übermittelt Lieferscheine und Rechnungen vollautomatisch – direkt aus Kalvero.</p>

  <div class="panel" style="left:370px;top:367px;width:334px;height:198px"></div>

  <h3 class="section-head" style="left:56px;top:396px">Vorteile auf einen Blick
    <svg width="230" height="30"><polyline points="0,29 205,29 228,4" fill="none" stroke="var(--blue)" stroke-width="1.5"/></svg></h3>
  <ul class="bullets" style="left:56px;top:434px;width:310px;line-height:22px">
    <li>Keine manuelle Erfassung von Bestellungen</li>
    <li>Direkte Integration in Kalvero ERP<br>(Wareneingang, Verkauf, Faktura)</li>
    <li>Automatisierte Kommunikation mit Partnern<br>wie Talvun, Useko, Ferna</li>
    <li>Fehlervermeidung durch standardisierte<br>Datenübermittlung</li>
    <li>Zeitersparnis und Entlastung der<br>Administration</li>
  </ul>

  <h3 class="section-head" style="left:391px;top:391px">So Funktioniert's</h3>
  <p class="body-text" style="left:391px;top:414px;width:260px">LinkEDI kommuniziert direkt mit den EDI-Systemen Ihrer Handelspartner. Sobald eine Bestellung eingeht, wird sie automatisch im Kalvero ERP angelegt. Genauso werden Lieferscheine und Rechnungen elektronisch erstellt und übermittelt – ohne Medienbrüche oder zusätzliche Eingaben.</p>

  <h3 class="section-head" style="left:391px;top:583px">Technische Voraussetzung
    <svg width="260" height="30"><polyline points="0,29 232,29 256,4" fill="none" stroke="var(--blue)" stroke-width="1.5"/></svg></h3>
  <ul class="bullets" style="left:391px;top:624px;width:300px;line-height:22px">
    <li>Kalvero ERP (KMU-Paket)</li>
    <li>Partnervereinbarung mit dem</li>
    <li>entsprechenden Handelspartner</li>
  </ul>

  <h3 class="section-head" style="left:391px;top:714px">Zielgruppe
    <svg width="230" height="30"><polyline points="0,29 200,29 224,4" fill="none" stroke="var(--blue)" stroke-width="1.5"/></svg></h3>
  <p class="body-text" style="left:391px;top:756px;width:280px">Lieferanten der Talvun, Useko, Ferna<br>oder anderer Grossverteiler</p>

  <div class="footer-black"></div>
  <div class="footer-blue"></div>

  <svg class="photo" style="left:4px;top:653px" width="352" height="280" role="img" aria-label="Foto: Hand am Laptop mit blauem Einkaufswagen-Symbol auf dem Bildschirm">
    <defs><linearGradient id="edi-bottom" x1="0" y1="0" x2="1" y2="1"><stop offset="0" stop-color="#cfd8e0"/><stop offset=".45" stop-color="#1a5e99"/><stop offset="1" stop-color="#2a2a2a"/></linearGradient></defs>
    <polygon points="90,3 262,3 348,140 262,277 90,277 4,140" fill="url(#edi-bottom)" stroke="#fff" stroke-width="6"/>
  </svg>

  <section class="company">
    <h2>Brendo Software GmbH,</h2>
    <ul class="contact">
      <li><svg width="11" height="14" viewBox="0 0 12 15"><path d="M6 0a6 6 0 0 0-6 6c0 4 6 9 6 9s6-5 6-9a6 6 0 0 0-6-6zm0 8.3A2.3 2.3 0 1 1 6 3.7a2.3 2.3 0 0 1 0 4.6z" fill="#fff"/></svg>Lindenweg 14, 7300 Feldhofen,</li>
      <li><svg width="12" height="12" viewBox="0 0 13 13"><circle cx="6.5" cy="6.5" r="6.5" fill="#fff"/><path d="M4 3.3l1.3 1.6-.7 1c.5 1 1.2 1.7 2.2 2.2l1-.7 1.6 1.3-.8 1.1C5.8 9.6 3.4 7.2 3.2 4.1z" fill="var(--blue)"/></svg>+41 81 555 01 23</li>
      <li><svg width="12" height="12" viewBox="0 0 13 13"><circle cx="6.5" cy="6.5" r="6.5" fill="#fff"/><rect x="3.3" y="4.3" width="6.4" height="4.4" fill="none" stroke="var(--blue)" stroke-width="1"/><polyline points="3.3,4.3 6.5,6.8 9.7,4.3" fill="none" stroke="var(--blue)" stroke-width="1"/></svg>info@brendo-software.example</li>
    </ul>
  </section>
</main>
</div>

<!-- Weapon reporting factsheet -->
<div class="sheet-slot slot-right">
<main class="flyer">
  <svg class="decor" width="704" height="993" aria-hidden="true">
    <polygon points="386,455 412,412 438,455" fill="var(--tri)"/>
    <polygon points="638,455 664,412 690,455" fill="var(--tri)"/>
    <polygon points="0,872 704,800 704,820 0,892" fill="var(--blue)"/>
  </svg>

  <div class="brand" style="left:194px;top:44px">
    <span class="brand-dot"></span>
    <div><div class="brand-name">BrendoSoftware</div><div class="brand-tag">BUSINESS &amp; SOFTWARE</div></div>
  </div>

  <h1 class="title" style="left:0;top:118px;width:704px;text-align:center;font-size:38px;line-height:46px"><span class="product">LinkMeldung –</span> Automatisierte<br>Waffenmeldung aus Kalvero</h1>

  <div class="band" style="top:233px;height:147px"></div>
  <p class="intro" style="left:56px;top:252px;width:330px;font-size:14px">Mit LinkMeldung bietet die Brendo Software GmbH eine clevere Lösung für Waffenhändler, um gesetzeskonforme Waffenmeldungen direkt aus dem ERP-System Kalvero an das Schweizer Online-Polizeiposten-System eVigil zu übermitteln – ganz ohne doppelte Erfassungen.</p>

  <svg class="photo" style="left:377px;top:233px" width="326" height="224" role="img" aria-label="Foto: Pistole liegt auf einem Formular mit Stift">
    <defs><linearGradient id="police-top" x1="0" y1="0" x2="1" y2="1"><stop offset="0" stop-color="#3a3a3a"/><stop offset=".45" stop-color="#d9d9d6"/><stop offset="1" stop-color="#4b4b44"/></linearGradient></defs>
    <polygon points="60,0 266,0 324,112 266,222 60,222 2,112" fill="url(#police-top)" stroke="#fff" stroke-width="4"/>
  </svg>

  <h3 class="section-head" style="left:56px;top:411px">Vorteile auf einen Blick
    <svg width="265" height="30"><polyline points="0,29 240,29 262,4" fill="none" stroke="var(--blue)" stroke-width="1.5"/></svg></h3>
  <ul class="bullets" style="left:56px;top:452px;width:290px;line-height:20.5px">
    <li>Kein Mehraufwand für gesetzliche<br>Waffenmeldungen</li>
    <li>Integration direkt in den Kalvero-Workflow<br>(Waren An- &amp; Verkauf)</li>
    <li>Automatisierte Übermittlung an Suisse<br>eVigil</li>
    <li>Weniger Fehler dank einmaliger, zentraler<br>Erfassung</li>
    <li>Zeitsparend &amp; rechtssicher</li>
  </ul>

  <h3 class="section-head" style="left:392px;top:516px">Technische Voraussetzung
    <svg width="260" height="30"><polyline points="0,29 232,29 256,4" fill="none" stroke="var(--blue)" stroke-width="1.5"/></svg></h3>
  <ul class="bullets" style="left:392px;top:558px;width:300px;line-height:24px">
    <li>Kalvero ERP (KMU-Paket)</li>
    <li>REST-API von Kalvero</li>
    <li>Zugang zu Suisse eVigil</li>
  </ul>

  <h3 class="section-head" style="left:392px;top:658px">Zielgruppe
    <svg width="230" height="30"><polyline points="0,29 200,29 224,4" fill="none" stroke="var(--blue)" stroke-width="1.5"/></svg></h3>
  <ul class="bullets" style="left:392px;top:700px;width:300px;line-height:22.5px">
    <li>Waffenhändler</li>
    <li>Fachgeschäfte mit Waffenverkauf</li>
    <li>Schützenverein</li>
    <li>Sicherheitsfirmen</li>
  </ul>

  <div class="footer-black"></div>
  <div class="footer-blue"></div>

  <svg class="photo" style="left:35px;top:653px" width="300" height="280" role="img" aria-label="Foto: Nahaufnahme einer schwarz-silbernen Pistole">
    <defs><linearGradient id="police-bottom" x1="0" y1="0" x2="1" y2="1"><stop offset="0" stop-color="#8d8d8d"/><stop offset=".5" stop-color="#3a3a3a"/><stop offset="1" stop-color="#111"/></linearGradient></defs>
    <polygon points="70,3 230,3 296,140 230,277 70,277 4,140" fill="url(#police-bottom)" stroke="#fff" stroke-width="6"/>
  </svg>

  <section class="company">
    <h2>Brendo Software GmbH,</h2>
    <ul class="contact">
      <li><svg width="11" height="14" viewBox="0 0 12 15"><path d="M6 0a6 6 0 0 0-6 6c0 4 6 9 6 9s6-5 6-9a6 6 0 0 0-6-6zm0 8.3A2.3 2.3 0 1 1 6 3.7a2.3 2.3 0 0 1 0 4.6z" fill="#fff"/></svg>Lindenweg 14, 7300 Feldhofen,</li>
      <li><svg width="12" height="12" viewBox="0 0 13 13"><circle cx="6.5" cy="6.5" r="6.5" fill="#fff"/><path d="M4 3.3l1.3 1.6-.7 1c.5 1 1.2 1.7 2.2 2.2l1-.7 1.6 1.3-.8 1.1C5.8 9.6 3.4 7.2 3.2 4.1z" fill="var(--blue)"/></svg>+41 81 555 01 23</li>
      <li><svg width="12" height="12" viewBox="0 0 13 13"><circle cx="6.5" cy="6.5" r="6.5" fill="#fff"/><rect x="3.3" y="4.3" width="6.4" height="4.4" fill="none" stroke="var(--blue)" stroke-width="1"/><polyline points="3.3,4.3 6.5,6.8 9.7,4.3" fill="none" stroke="var(--blue)" stroke-width="1"/></svg>info@brendo-software.example</li>
    </ul>
  </section>
</main>
</div>

</body>
</html>
```